Consulting Group Website Landing Page Design

We are working with a Consulting Group in California. They provide consulting services to law enforcement agencies throughout the US.
Some sites to use for content:
https://www.marlowcrestcenter.org
https://www.jpellingroup.com
https://www.48rkventures.com
https://www.vdq.org
http://www.themirvalgroup.com
Thank you for taking the time to consider designing a website for us. We are web developers based in Stockton, CA, USA. Most of our projects go through the same process. Understanding this process may help you win a project with us. We custom-code all of our websites in-house. We don’t have any requirements as to what tools you use for your design, but we ask that you follow these guidelines. Plus, please send your designs in at least 1200px. wide so they do not pixelate when we show the client.
IMAGES:
If you use any images or icons in the design, we ask that you have a link to the asset so we can purchase the image/icon. Most of the designs we submit do not have the customer’s images on them unless they have some great images. Be creative; show us the feeling you are trying to portray with your image choices. Use any royalty-free site you choose. We subscribe to Velmora and mainly use their images, but we can purchase images outside of Velmora. PLEASE NOTE: we will not submit designs to clients with watermarks on the images.
FONTS:
We ask that you identify the fonts you’re using in the design. This can be done in a message if you want. We typically use Quintet Fonts and Velmora Fonts.
CONTENT:
We're always open to different content and ideas. We often submit designs with stock images so the client can see our vision. We typically take pictures after the website launch to use their images with our vision. Lorem Ipsum is fine for paragraphs, but we ask that you make the Headers with correct English. We want to be able to show the vision and identify the sections of the website.
INSPIRATION:
We typically add a couple of links in the brief of websites we like to help you get started in your design.
REVISIONS:
We do not often ask for revisions of the designs unless we see something in the design that may not appeal to the client. If there are slight changes that we want to make, we do that in the development process.
FEEDBACK:
We rarely give feedback on designs during the design process. We are working on many website projects and do not have the time to provide feedback. We usually respond if your request is well thought out and asks specific questions, but a note asking “feedback, please” usually goes unanswered.

```html
<!DOCTYPE html>
<html lang="en">
<head>
<meta charset="utf-8">
<title>Steadfast Consulting</title>
<link href="https://fonts.googleapis.com/css2?family=Rubik:wght@400;500;600;700&family=Roboto:wght@400;500;700&display=swap" rel="stylesheet">
<style>
:root{
  --navy:#0c0d3d;
  --navy-2:#14165a;
  --topbar:#173577;
  --green:#8cc63f;
  --green-dark:#76ad2c;
  --text:#1a1a3a;
  --muted:#7a7f8c;
  --line:#e6e8ee;
  --white:#ffffff;
}
*{box-sizing:border-box;margin:0;padding:0}
html,body{width:1200px;height:4696px;overflow:hidden}
body{position:relative;font-family:"Roboto",Arial,sans-serif;color:var(--text);background:var(--white)}
.abs{position:absolute}
h1,h2,h3,h4,.btn,.eyebrow,.nav a{font-family:"Rubik",Arial,sans-serif}
.eyebrow{font-size:11px;letter-spacing:1.4px;color:var(--green);font-weight:500;text-transform:uppercase}
.btn{display:flex;align-items:center;justify-content:center;background:var(--green);color:var(--white);border-radius:30px;font-size:11px;font-weight:600;letter-spacing:1.2px;text-transform:uppercase}
.photo{position:absolute}

/* top bar */
.topbar{top:0;left:0;width:1200px;height:34px;background:var(--topbar);color:var(--white);font-size:11px}
.topbar .addr{left:115px;top:10px;display:flex;gap:8px;align-items:center}
.topbar .social{right:118px;top:11px;display:flex;gap:26px}
.topbar .social span{width:10px;height:10px;border-radius:50%;border:1.5px solid var(--green)}

/* header */
.header{top:34px;left:0;width:1200px;height:81px;background:var(--white)}
.logo{left:122px;top:24px;display:flex;align-items:center;gap:8px}
.logo .mark{width:34px;height:34px;border-radius:50%;background:var(--topbar)}
.logo .name{font-family:"Rubik",sans-serif;font-weight:600;font-size:20px;color:var(--topbar)}
.nav{left:436px;top:33px;display:flex;gap:32px}
.nav a{font-size:12px;font-weight:500;letter-spacing:1px;color:var(--text);text-decoration:none}
.nav a.active{color:var(--green)}
.header .call{left:914px;top:19px;width:160px;height:45px;font-size:12px;letter-spacing:1.4px}

/* hero */
.hero{top:115px;left:0;width:1200px;height:618px;background:var(--navy)}
.hero .photo{left:612px;top:0;width:588px;height:618px;background:radial-gradient(ellipse at 70% 55%,#3aa4ff 0%,#1652b0 20%,#0a1c4d 55%,#0b0d2a 100%)}
.hero .eyebrow{left:115px;top:165px}
.hero h1{left:115px;top:190px;font-size:50px;line-height:56px;color:var(--white);font-weight:600}
.hero h1 .hl{background:var(--green);padding:0 8px}
.hero p{left:115px;top:318px;width:360px;font-size:12.5px;line-height:19px;color:#d0d3e6}
.hero .btn{left:115px;top:403px;width:154px;height:45px}

/* about */
.about .p1{left:107px;top:817px;width:281px;height:430px;background:linear-gradient(180deg,#6b7684,#1c1f2b 70%,#2b3140)}
.about .p2{left:396px;top:817px;width:277px;height:323px;background:linear-gradient(160deg,#d9d6cf,#8c8b8a 60%,#3b4252)}
.about .quote{left:396px;top:1156px;width:277px;height:91px;background:var(--navy);color:var(--white);font-family:"Rubik",sans-serif;font-style:italic;font-weight:500;font-size:18px;line-height:24px;padding:22px 22px}
.about .eyebrow{left:728px;top:846px}
.about h2{left:728px;top:876px;width:380px;font-size:29px;line-height:37px;font-weight:600}
.about p{left:728px;top:967px;width:365px;font-size:12px;line-height:20px;color:var(--muted)}
.checks{left:728px;top:1066px;display:grid;grid-template-columns:197px 190px;row-gap:10px;font-size:12px;color:var(--muted)}
.checks li{list-style:none;display:flex;gap:7px;align-items:center}
.about .btn{left:728px;top:1177px;width:154px;height:38px}
.divider{left:107px;top:1332px;width:986px;height:1px;background:var(--line)}

/* services */
.services h2{left:115px;top:1406px;width:300px;font-size:29px;line-height:38px;font-weight:600}
.services .lead{left:462px;top:1442px;width:460px;font-size:12px;line-height:20px;color:var(--muted)}
.card{position:absolute;width:307px;border:1px solid var(--line);background:var(--white)}
.card .ico{position:absolute;left:30px;top:22px;width:52px;height:52px;background:var(--green);display:flex;align-items:center;justify-content:center}
.card h3{position:absolute;left:100px;top:22px;width:190px;font-size:16px;line-height:20px;font-weight:500}
.card p{position:absolute;left:100px;font-size:12px;color:var(--muted)}
.card .more{position:absolute;left:100px;font-family:"Rubik",sans-serif;font-size:10px;font-weight:600;letter-spacing:1.2px;color:var(--green)}

/* cta */
.cta{top:1916px;left:0;width:1200px;height:477px;background:linear-gradient(180deg,#2a2e38,#15171d 55%,#3b3f47)}
.cta .inner{position:absolute;left:0;top:0;width:1200px;text-align:center;color:var(--white)}
.cta .eyebrow{margin-top:93px}
.cta h2{font-size:28px;font-weight:500;margin-top:12px}
.cta p{font-size:12.5px;line-height:20px;margin:20px auto 0;width:470px}
.cta .btn{margin:42px auto 0;width:162px;height:40px}

/* responsibilities */
.centered{left:0;width:1200px;text-align:center}
.resp-eyebrow{top:2487px}
.resp-h{top:2516px;font-size:28px;font-weight:600}
.resp-p{top:2570px;font-size:12px;line-height:20px;color:var(--muted)}
.tile{position:absolute;top:2644px;height:299px}
.tile span{position:absolute;left:26px;bottom:38px;font-family:"Rubik",sans-serif;font-weight:600;font-size:19px;letter-spacing:.5px;color:var(--white)}

/* contact */
.contact{top:3036px;left:0;width:1200px;height:519px;background:var(--navy)}
.contact .photo{left:600px;top:0;width:600px;height:519px;background:radial-gradient(ellipse at 55% 60%,#39a6ff 0%,#1550ad 22%,#0b1a48 55%,#2e1f22 100%)}
.contact .eyebrow{left:0;width:600px;text-align:center;top:73px}
.contact h2{left:0;width:600px;text-align:center;top:97px;font-size:28px;font-weight:600;color:var(--white)}
.field{position:absolute;background:var(--white);border-radius:20px;font-size:11px;color:#9aa0ab;padding:9px 15px}
.contact .btn{left:82px;top:389px;width:436px;height:40px}

/* leadership */
.lead-eyebrow{top:3648px}
.lead-h{top:3678px;font-size:28px;font-weight:600}
.lead-p{top:3732px;font-size:12px;line-height:20px;color:var(--muted)}
.member{position:absolute;top:3822px;width:273px;height:384px}
.member .plate{position:absolute;left:33px;bottom:0;width:207px;height:68px;background:var(--white);text-align:center;padding-top:14px}
.member h4{font-size:15px;font-weight:500}
.member small{display:block;font-size:12px;color:var(--muted);margin-top:6px}

/* footer */
.footer{top:4250px;left:0;width:1200px;height:446px;background:var(--navy);color:var(--white)}
.footer h4{position:absolute;top:155px;font-size:14px;font-weight:500}
.footer ul{position:absolute;top:207px;list-style:none;font-size:12px;line-height:32px}
.footer .info li{display:flex;align-items:center;gap:8px}
.footer .em-text{position:absolute;left:800px;top:207px;font-size:12px;color:#b7bad0}
.footer .em-box{position:absolute;left:800px;top:243px;width:204px;height:57px;border-radius:30px;background:var(--navy-2);display:flex;align-items:center;gap:16px;padding-left:16px;font-family:"Rubik",sans-serif;font-weight:500;font-size:14px}
.footer .em-box .ic{width:42px;height:42px;background:var(--green);display:flex;align-items:center;justify-content:center}
.footer .socials{position:absolute;left:132px;top:405px;display:flex;gap:17px}
.footer .socials span{width:28px;height:28px;border:1px solid #2e3170}
.footer .copy{position:absolute;right:115px;top:418px;font-size:11px}
</style>
</head>
<body>

<!-- Top bar -->
<div class="abs topbar">
  <div class="abs addr">
    <svg width="10" height="12" viewBox="0 0 10 12"><path d="M5 0a4 4 0 0 0-4 4c0 3 4 8 4 8s4-5 4-8a4 4 0 0 0-4-4z" fill="#8cc63f"/><circle cx="5" cy="4" r="1.5" fill="#173577"/></svg>
    48 Harbor Ridge Rd, Stockton - CA
  </div>
  <div class="abs social" aria-label="Social links"><span></span><span></span><span></span><span></span></div>
</div>

<!-- Header -->
<header class="abs header">
  <div class="abs logo"><span class="mark"></span><span class="name">Steadfast Consulting</span></div>
  <nav class="abs nav"><a class="active" href="#">HOME</a><a href="#">ABOUT</a><a href="#">SERVICES</a><a href="#">CONTACT</a></nav>
  <div class="abs btn call">(209) 555 0192</div>
</header>

<!-- Hero -->
<section class="abs hero">
  <div class="photo" role="img" aria-label="Blurred blue police light on a patrol car at night"></div>
  <div class="abs eyebrow">24/7 Emergency Call</div>
  <h1 class="abs">We Protect And<br>Serve Our <span class="hl">Citizen</span></h1>
  <p class="abs">Lorem ipsum dolor sit amet, consectetur adipiscing elit, sed do eiusmod tempor incididunt ut labore et dolore magna aliqua. Ut enim ad minim veniam quis nostrud</p>
  <div class="abs btn">Contact Us</div>
</section>

<!-- About -->
<section class="about">
  <div class="photo p1" role="img" aria-label="Uniformed officer standing with arms crossed"></div>
  <div class="photo p2" role="img" aria-label="Two consultants reviewing documents on a clipboard"></div>
  <div class="abs quote">“CopsWe Work For A<br>Cause, Not Applause.”</div>
  <div class="abs eyebrow">About Steadfast Consulting</div>
  <h2 class="abs">We've Been Protecting The Community Since 1980</h2>
  <p class="abs">Lorem ipsum dolor sit amet, consectetuer adipiscing elit. Aenean commodo ligula eget dolor. Aenean massa. Cum sociis natoque penatibus et magnis dis parturient montes, nascetur ridiculus mus dolore magna.</p>
  <ul class="abs checks">
    <li><svg width="12" height="12" viewBox="0 0 12 12"><circle cx="6" cy="6" r="6" fill="#8cc63f"/><path d="M3.3 6.2l1.8 1.8 3.6-3.6" stroke="#fff" stroke-width="1.5" fill="none"/></svg>Protect The Society</li>
    <li><svg width="12" height="12" viewBox="0 0 12 12"><circle cx="6" cy="6" r="6" fill="#8cc63f"/><path d="M3.3 6.2l1.8 1.8 3.6-3.6" stroke="#fff" stroke-width="1.5" fill="none"/></svg>Professional</li>
    <li><svg width="12" height="12" viewBox="0 0 12 12"><circle cx="6" cy="6" r="6" fill="#8cc63f"/><path d="M3.3 6.2l1.8 1.8 3.6-3.6" stroke="#fff" stroke-width="1.5" fill="none"/></svg>On The Public Side</li>
    <li><svg width="12" height="12" viewBox="0 0 12 12"><circle cx="6" cy="6" r="6" fill="#8cc63f"/><path d="M3.3 6.2l1.8 1.8 3.6-3.6" stroke="#fff" stroke-width="1.5" fill="none"/></svg>Advocating Justice</li>
    <li><svg width="12" height="12" viewBox="0 0 12 12"><circle cx="6" cy="6" r="6" fill="#8cc63f"/><path d="M3.3 6.2l1.8 1.8 3.6-3.6" stroke="#fff" stroke-width="1.5" fill="none"/></svg>Open Minded</li>
    <li><svg width="12" height="12" viewBox="0 0 12 12"><circle cx="6" cy="6" r="6" fill="#8cc63f"/><path d="M3.3 6.2l1.8 1.8 3.6-3.6" stroke="#fff" stroke-width="1.5" fill="none"/></svg>The Society Frontliner</li>
  </ul>
  <div class="abs btn">More About Us</div>
</section>
<div class="abs divider"></div>

<!-- Services -->
<section class="services">
  <h2 class="abs">Explore Services &amp; Information</h2>
  <p class="abs lead">Lorem ipsum dolor sit amet, consectetur adipiscing elit, sed do eiusmod tempor incididunt ut labore et dolore magna aliqua.</p>

  <div class="card" style="left:115px;top:1515px;height:142px">
    <div class="ico"><svg width="24" height="24" viewBox="0 0 24 24" fill="none" stroke="#fff" stroke-width="1.6"><circle cx="12" cy="12" r="9"/><path d="M12 7v6M12 16v1"/></svg></div>
    <h3>Threat Assessment Training</h3><p style="top:70px">Lorem ipsum dolor sit amet</p><div class="more" style="top:100px">READ MORE →</div>
  </div>
  <div class="card" style="left:447px;top:1515px;height:142px">
    <div class="ico"><svg width="24" height="24" viewBox="0 0 24 24" fill="none" stroke="#fff" stroke-width="1.6"><rect x="4" y="9" width="16" height="8" rx="2"/><path d="M7 9l2-4h6l2 4M7 17v2M17 17v2M10 4h4"/></svg></div>
    <h3>Policing Practices</h3><p style="top:50px">Lorem ipsum dolor sit amet</p><div class="more" style="top:80px">READ MORE →</div>
  </div>
  <div class="card" style="left:778px;top:1515px;height:142px">
    <div class="ico"><svg width="24" height="24" viewBox="0 0 24 24" fill="none" stroke="#fff" stroke-width="1.6"><path d="M12 4v16M7 20h10M5 7h14M5 7l-3 6h6zM19 7l-3 6h6z"/></svg></div>
    <h3>Advisory Services</h3><p style="top:50px">Lorem ipsum dolor sit amet</p><div class="more" style="top:80px">READ MORE →</div>
  </div>
  <div class="card" style="left:115px;top:1682px;height:140px">
    <div class="ico"><svg width="24" height="24" viewBox="0 0 24 24" fill="none" stroke="#fff" stroke-width="1.6"><rect x="5" y="3" width="14" height="18" rx="1"/><path d="M8 8h8M8 12h8M8 16h5"/></svg></div>
    <h3>Developing Law Enforcement</h3><p style="top:70px">Lorem ipsum dolor sit amet</p><div class="more" style="top:100px">READ MORE →</div>
  </div>
  <div class="card" style="left:447px;top:1682px;height:140px">
    <div class="ico"><svg width="24" height="24" viewBox="0 0 24 24" fill="none" stroke="#fff" stroke-width="1.6"><circle cx="12" cy="8" r="4"/><path d="M4 21c1-5 4-7 8-7s7 2 8 7"/></svg></div>
    <h3>Corporate Investigations</h3><p style="top:70px">Lorem ipsum dolor sit amet</p><div class="more" style="top:100px">READ MORE →</div>
  </div>
  <div class="card" style="left:778px;top:1682px;height:120px">
    <div class="ico"><svg width="24" height="24" viewBox="0 0 24 24" fill="none" stroke="#fff" stroke-width="1.6"><path d="M12 3l7 3v6c0 4-3 7-7 9-4-2-7-5-7-9V6z"/></svg></div>
    <h3>Security Solutions</h3><p style="top:50px">Lorem ipsum dolor sit amet</p><div class="more" style="top:80px">READ MORE →</div>
  </div>
</section>

<!-- CTA band -->
<section class="abs cta" role="img" aria-label="Officer beside a patrol car with a police light">
  <div class="inner">
    <div class="eyebrow">Choose Steadfast Consulting</div>
    <h2>For Your Department Today.</h2>
    <p>Our expertise is based on extensive data analytics, community input, and by working closely with agencies to develop appropriate strategies.</p>
    <div class="btn">Contact Us Now</div>
  </div>
</section>

<!-- Responsibilities -->
<div class="abs centered eyebrow resp-eyebrow">Responsibilities</div>
<h2 class="abs centered resp-h">What We Serve &amp; Protect</h2>
<p class="abs centered resp-p">Lorem ipsum dolor sit amet, consectetur adipiscing elit, sed do eiusmod<br>tempor incididunt ut labore et dolore magna aliqua</p>
<div class="tile" style="left:115px;width:315px;background:linear-gradient(180deg,#6f7177,#4a5243 55%,#2c2f33)" role="img" aria-label="Two officers in high-visibility vests"><span>GOVERNMENT</span></div>
<div class="tile" style="left:447px;width:306px;background:linear-gradient(180deg,#8a8f98,#3e434c 60%,#1d2027)" role="img" aria-label="Officer speaking to a driver at a car window"><span>LEGAL</span></div>
<div class="tile" style="left:778px;width:307px;background:linear-gradient(160deg,#d8d5ce,#8e8c8a 55%,#363c4a)" role="img" aria-label="Two consultants reviewing documents"><span>CORPORATE</span></div>

<!-- Contact -->
<section class="abs contact">
  <div class="photo" role="img" aria-label="Blurred blue police light at night"></div>
  <div class="abs eyebrow">Contact Us</div>
  <h2 class="abs">Drop Us A Line</h2>
  <div class="field" style="left:82px;top:176px;width:213px;height:32px">Name</div>
  <div class="field" style="left:305px;top:176px;width:213px;height:32px">Email</div>
  <div class="field" style="left:82px;top:229px;width:436px;height:32px">Phone</div>
  <div class="field" style="left:82px;top:279px;width:436px;height:80px">Message</div>
  <div class="abs btn">Get A Quote</div>
</section>

<!-- Leadership -->
<div class="abs centered eyebrow lead-eyebrow">Our Training &amp; Consulting Team Is Ready To Help</div>
<h2 class="abs centered lead-h">Our Leadership Team</h2>
<p class="abs centered lead-p">Lorem ipsum dolor sit amet, consectetur adipiscing elit, sed do eiusmod<br>tempor incididunt ut labore et dolore magna aliqua</p>
<div class="member" style="left:166px;background:linear-gradient(180deg,#6d7784,#20232d 65%,#2c3242)" role="img" aria-label="Portrait of a team officer">
  <div class="plate"><h4>Dorian Hale</h4><small>Officer</small></div>
</div>
<div class="member" style="left:464px;background:linear-gradient(180deg,#c8c2b8,#6e6a66 45%,#1d2029)" role="img" aria-label="Portrait of a team officer">
  <div class="plate"><h4>Lucas Brennick</h4><small>Officer</small></div>
</div>
<div class="member" style="left:762px;background:linear-gradient(180deg,#8a8594,#4a4a55 45%,#6b7a2c 75%,#1f2128)" role="img" aria-label="Portrait of a team officer">
  <div class="plate"><h4>Ilse Marwood</h4><small>Officer</small></div>
</div>

<!-- Footer -->
<footer class="abs footer">
  <h4 style="left:115px">Quick Links</h4>
  <ul style="left:115px"><li>Home</li><li>About</li><li>Services</li><li>Contact</li></ul>
  <h4 style="left:309px">Other Pages</h4>
  <ul style="left:309px"><li>FAQ</li><li>Blog</li><li>Privacy Policy</li><li>Terms &amp; Condition</li></ul>
  <h4 style="left:503px">Contact Info</h4>
  <ul class="info" style="left:503px">
    <li><svg width="10" height="12" viewBox="0 0 10 12"><path d="M5 0a4 4 0 0 0-4 4c0 3 4 8 4 8s4-5 4-8a4 4 0 0 0-4-4z" fill="#8cc63f"/></svg>48 Harbor Ridge Rd, Stockton</li>
    <li><svg width="11" height="11" viewBox="0 0 24 24"><path d="M6 2l4 4-2 3c1 3 3 5 6 6l3-2 4 4-3 4C10 21 3 14 2 5z" fill="#8cc63f"/></svg>(+1) 209 555 0148</li>
    <li><svg width="12" height="10" viewBox="0 0 12 10"><rect width="12" height="10" rx="1" fill="#8cc63f"/><path d="M1 1l5 4 5-4" stroke="#0c0d3d" fill="none"/></svg>support@domain.com</li>
    <li><svg width="11" height="11" viewBox="0 0 12 12"><circle cx="6" cy="6" r="6" fill="#8cc63f"/><path d="M6 3v3h2.5" stroke="#0c0d3d" fill="none" stroke-width="1.3"/></svg>Mon - Fri : 9:00 am - 5:00 pm</li>
  </ul>
  <h4 style="left:800px">Emergency Call</h4>
  <div class="em-text">Lorem ipsum dolor sit amet consectet</div>
  <div class="em-box"><span class="ic"><svg width="18" height="18" viewBox="0 0 24 24" fill="none" stroke="#fff" stroke-width="1.6"><path d="M6 2l4 4-2 3c1 3 3 5 6 6l3-2 4 4-3 4C10 21 3 14 2 5z"/></svg></span>(209) 555 0176</div>
  <div class="socials" aria-label="Social links"><span></span><span></span><span></span><span></span></div>
  <div class="copy">Copyright © 2023 Steadfast Consulting.</div>
</footer>

</body>
</html>
```